Social media design templates

A variety of templates incorporating our logo and colours to use for our postings on different social media platforms. Must be user friendly and meet our brand image. We have attached our logo to view. We would like some of the templates to offer the ability to insert a background image and others to be a template designed around our logo.

We are black and white in colour, and our values speak to our transparency and honesty, so we are looking for clean cut, sharp straight lines, not using any other colours or curved lines.

We are a recruitment company that will be using these templates
- job posting,
- general announcements,
- blog,
- company newsletter,
- updates,
- testimonials and
- top candidate profiles

We would like a gallery of templates to choose from to use separately that all represent our brand.

```html
<!DOCTYPE html>
<html lang="en">
<head>
<meta charset="utf-8">
<title>Norvale – Social media design templates</title>
<link href="https://fonts.googleapis.com/css2?family=Work+Sans:ital,wght@0,400;0,500;0,600;1,400&display=swap" rel="stylesheet">
<style>
  :root {
    --ink: #0b0b0e;
    --paper: #ffffff;
    --muted: #8c9590;
    --shadow: rgba(0,0,0,0.28);
    --photo-a: #3e4842;
    --photo-b: #6e5c4a;
    --portrait-a: #9c8a82;
    --portrait-b: #b8643c;
  }
  * { margin: 0; padding: 0; box-sizing: border-box; }
  html, body { width: 1200px; height: 649px; overflow: hidden; background: var(--paper); }
  body { position: relative; font-family: "Work Sans", Arial, sans-serif; color: var(--ink); }

  .brand-panel { position: absolute; left: 0; top: 0; width: 279px; height: 546px; background: var(--ink); color: var(--paper); }
  .brand-name { position: absolute; left: 31px; top: 104px; font-weight: 600; font-size: 26px; letter-spacing: 0.5px; }
  .panel-title { position: absolute; left: 32px; top: 143px; font-weight: 500; font-size: 20px; line-height: 21px; letter-spacing: 1px; }

  .formats-label { position: absolute; left: 18px; top: 555px; font-size: 11px; letter-spacing: 0.3px; }
  .tool { position: absolute; top: 601px; display: flex; align-items: center; gap: 5px; font-size: 11px; font-weight: 500; line-height: 14px; }
  .tool-pixelry { left: 24px; }
  .tool-layoutly { left: 90px; }
  .tool-shape { width: 12px; height: 12px; background: var(--ink); }
  .tool-shape--round { border-radius: 50%; }
  .formats-extra { position: absolute; left: 166px; top: 590px; font-size: 18px; line-height: 18px; }

  .card { position: absolute; width: 201px; height: 201px; background: var(--paper); box-shadow: 2px 3px 4px var(--shadow); overflow: hidden; }
  .card--dark { background: var(--ink); color: var(--paper); }
  .photo { position: absolute; background: linear-gradient(160deg, var(--photo-a), #55584c 55%, var(--photo-b)); }
  .portrait { position: absolute; background: radial-gradient(circle at 50% 45%, var(--portrait-a), #8e7a70 60%, var(--portrait-b)); box-shadow: 1px 2px 3px var(--shadow); }
  .tri { position: absolute; background: var(--ink); }
  .tri--bl { clip-path: polygon(0 0, 0 100%, 100% 100%); }
  .tri--tl { clip-path: polygon(0 0, 100% 0, 0 100%); }
  .tri--tr { clip-path: polygon(0 0, 100% 0, 100% 100%); }
  .tri--light { background: var(--paper); }
  .mark { position: absolute; font-weight: 600; font-size: 13px; letter-spacing: 0.3px; }
  .mark-box { position: absolute; display: flex; align-items: center; justify-content: center; font-weight: 600; font-size: 6px; }
  .mark-box--dark { background: var(--ink); color: var(--paper); box-shadow: 1px 2px 3px var(--shadow); }
  .mark-box--light { background: var(--paper); color: var(--ink); }

  .newsletter { left: 317px; top: 85px; }
  .newsletter .heading { position: absolute; left: 12px; top: 110px; font-weight: 600; font-size: 11px; letter-spacing: 0.4px; }

  .announce { left: 532px; top: 85px; }
  .announce .heading { position: absolute; left: 110px; top: 17px; font-weight: 600; font-size: 7px; line-height: 8px; letter-spacing: 0.5px; }

  .team-grid { left: 743px; top: 85px; background: var(--ink); }
  .team-grid .inner { position: absolute; left: 7px; top: 7px; right: 7px; bottom: 7px; background: var(--paper); }
  .tile { position: absolute; width: 74px; height: 74px; box-shadow: 1px 2px 3px var(--shadow); }
  .tile .role { position: absolute; left: 0; right: 0; bottom: 0; height: 7px; background: var(--ink); color: var(--paper); font-size: 3.5px; text-align: center; line-height: 7px; }
  .tile--brand { background: var(--ink); color: var(--paper); display: flex; align-items: center; justify-content: center; font-weight: 600; font-size: 12px; }

  .testimonial { left: 955px; top: 85px; height: 198px; }
  .testimonial .quote-mark { position: absolute; left: 98px; top: 32px; font-size: 30px; font-weight: 600; color: var(--muted); line-height: 30px; }
  .testimonial .quote { position: absolute; left: 103px; top: 58px; font-style: italic; font-size: 14px; line-height: 14px; letter-spacing: 0.3px; }
  .testimonial .author { position: absolute; right: 14px; top: 134px; font-weight: 600; font-size: 6px; }

  .top-candidate { left: 317px; top: 342px; }
  .top-candidate .inner { position: absolute; left: 17px; top: 17px; width: 168px; height: 167px; background: var(--ink); color: var(--paper); }
  .top-candidate .heading { position: absolute; left: 11px; top: 7px; font-weight: 600; font-size: 10px; }
  .top-candidate .note { position: absolute; left: 10px; top: 104px; font-style: italic; font-size: 6px; }

  .blog { left: 532px; top: 342px; }
  .blog .heading { position: absolute; left: 0; right: 0; top: 116px; text-align: center; font-weight: 500; font-size: 10px; letter-spacing: 0.6px; padding-left: 14px; }

  .update { left: 754px; top: 342px; }
  .update .heading { position: absolute; left: 18px; top: 108px; font-weight: 600; font-size: 10px; letter-spacing: 0.6px; }

  .footer-mark { position: absolute; left: 1080px; top: 586px; font-weight: 600; font-size: 26px; letter-spacing: 0.5px; }
</style>
</head>
<body>

<section class="brand-panel">
  <div class="brand-name">Norvale</div>
  <h1 class="panel-title">Social media<br>design templates</h1>
</section>

<p class="formats-label">Editable format files</p>
<div class="tool tool-pixelry"><span class="tool-shape"></span>Pixelry</div>
<div class="tool tool-layoutly"><span class="tool-shape tool-shape--round"></span>Layoutly</div>
<p class="formats-extra">+ PNG<br>&amp; JPEG</p>

<article class="card newsletter">
  <div class="photo" style="left:0;top:0;width:201px;height:100px" role="img" aria-label="Photo of colleagues laughing around laptops at a table"></div>
  <h2 class="heading">Newsletter</h2>
  <div class="tri tri--bl" style="left:10px;top:174px;width:17px;height:17px"></div>
  <div class="mark" style="right:12px;top:174px">Norvale</div>
</article>

<article class="card card--dark announce">
  <div class="photo" style="left:0;top:0;width:102px;height:201px" role="img" aria-label="Photo of two colleagues smiling beside a laptop"></div>
  <div class="tri tri--tl" style="left:8px;top:8px;width:26px;height:26px"></div>
  <div class="tri tri--tr" style="left:82px;top:8px;width:14px;height:14px"></div>
  <h2 class="heading">General<br>Announcements</h2>
  <div class="mark" style="left:11px;top:174px">Norvale</div>
</article>

<article class="card team-grid">
  <div class="inner">
    <div class="tile photo" style="left:15px;top:16px" role="img" aria-label="Photo of a team around a desk"><span class="role">Sales Manager</span></div>
    <div class="tile photo" style="left:98px;top:16px" role="img" aria-label="Photo of colleagues at a laptop"><span class="role">Civil Site Manager</span></div>
    <div class="tile photo" style="left:15px;top:97px" role="img" aria-label="Photo of three colleagues laughing outdoors"><span class="role">State Manager</span></div>
    <div class="tile tile--brand" style="left:98px;top:97px">Norvale</div>
  </div>
</article>

<article class="card testimonial">
  <div class="tri tri--tl" style="left:13px;top:7px;width:13px;height:13px"></div>
  <div class="portrait" style="left:14px;top:46px;width:73px;height:72px" role="img" aria-label="Portrait photo of a smiling candidate"></div>
  <div class="quote-mark">“</div>
  <p class="quote">testimonial<br>text here</p>
  <p class="author">Nora Vale</p>
  <div class="mark-box mark-box--dark" style="left:14px;top:141px;width:33px;height:32px">Norvale</div>
</article>

<article class="card top-candidate">
  <div class="inner">
    <h2 class="heading">Top</h2>
    <div class="portrait" style="left:49px;top:21px;width:71px;height:72px" role="img" aria-label="Portrait photo of the featured candidate"></div>
    <div class="tri tri--tr tri--light" style="left:146px;top:9px;width:12px;height:12px"></div>
    <p class="note">Text here</p>
    <div class="mark-box mark-box--light" style="left:140px;top:140px;width:22px;height:22px;font-size:4.5px">Norvale</div>
  </div>
</article>

<article class="card card--dark blog">
  <div class="photo" style="left:0;top:0;width:201px;height:108px" role="img" aria-label="Photo of colleagues laughing around laptops at a table"></div>
  <div class="tri tri--tl" style="left:6px;top:8px;width:26px;height:26px"></div>
  <div class="tri tri--tr" style="left:158px;top:8px;width:35px;height:35px"></div>
  <h2 class="heading">New in our blog</h2>
  <div class="mark" style="left:15px;top:144px">Norvale</div>
</article>

<article class="card update">
  <div class="photo" style="left:18px;top:21px;width:163px;height:77px" role="img" aria-label="Photo of colleagues laughing around laptops at a table"></div>
  <h2 class="heading">UPDATE</h2>
  <div class="tri tri--tl" style="left:18px;top:123px;width:15px;height:15px"></div>
  <div class="mark-box mark-box--dark" style="left:149px;top:109px;width:32px;height:32px">Norvale</div>
</article>

<div class="footer-mark">Norvale</div>

</body>
</html>
```